Business Card Design

I have a very clear idea of what I want. I just do not know how to do the graphic design to match it.

On the front I want the uploaded image with the horse and the two people.
I want

Bottom left hand corner
Lewis Brand
0438 512 607

Bottom right
There is maroon block with Neil Patton Practitioner Group Logo
Next to that I want the Stable Arc tile about the same size ( attached psd file)

On the back I want a plain colour (white) with the information

Lewis Brand
Equine Performance
Rowland4Ponies and Acupuncture
Horsemanship Lessons and Clinics
Horse Training

lbrand@fauna812.com.au
FB/lewis.brand.207
StableArc.com.au

Industry/Entity Type

Business

Contact Information for Business Card

Lewis Brand
0438 512 607
lbrand@fauna812.com.au

```html
<!DOCTYPE html>
<html lang="en">
<head>
<meta charset="utf-8">
<title>Stable Arc – Business Card</title>
<link rel="stylesheet" href="https://fonts.googleapis.com/css2?family=Open+Sans:wght@400;600&family=Cormorant+Garamond:wght@500&family=Great+Vibes&display=swap">
<style>
  :root{
    --bg:#d9d9d6;
    --cream:#ece4d6;
    --navy:#1f3d73;
    --navy-dark:#17305c;
    --white:#ffffff;
    --brown:#5b3a24;
    --maroon:#7a2e12;
    --sand-light:#d9c08f;
    --sand-mid:#c4a46c;
    --sand-dark:#a88a57;
    --ink:#3a2a1a;
  }
  *{margin:0;padding:0;box-sizing:border-box}
  html,body{width:1200px;height:873px;overflow:hidden;background:var(--bg)}
  body{font-family:"Open Sans",Arial,sans-serif;position:relative}
  .card{position:absolute;top:271px;width:540px;height:330px;border-radius:4px;overflow:hidden;box-shadow:0 6px 18px rgba(0,0,0,.18)}
  .card--back{left:40px;background:var(--cream)}
  .card--front{left:620px;border:5px solid var(--navy)}

  /* Back */
  .brand-tile{position:absolute;left:34px;top:28px;width:118px;height:100px;border-radius:20px;background:var(--white);border:6px solid var(--brown);display:flex;align-items:center;justify-content:center;gap:7px}
  .brand-tile__mark{width:14px;height:14px;background:var(--navy)}
  .brand-tile__name{font-weight:600;font-size:15px;color:var(--navy)}
  .contact{position:absolute;left:34px;display:flex;flex-direction:column;gap:10px}
  .contact--top{top:160px}
  .contact--bottom{top:250px}
  .contact__row{display:flex;align-items:center;gap:10px;font-size:13px;color:var(--navy)}
  .icon{width:24px;height:24px;flex:none}
  .details{position:absolute;right:24px;top:130px;width:250px;background:var(--navy);border-radius:22px;padding:16px 20px;color:var(--white)}
  .details__name{font-size:21px;font-weight:400;margin-bottom:6px}
  .details__list{list-style:none;font-size:12.5px;line-height:1.45}
  .details__list li{display:flex;gap:6px;align-items:center}
  .details__list svg{width:11px;height:11px;flex:none}

  /* Front */
  .photo{position:absolute;inset:0;background:radial-gradient(ellipse at 60% 60%,var(--sand-light),var(--sand-mid) 60%,var(--sand-dark))}
  .headline{position:absolute;right:30px;top:22px;text-align:center;color:var(--ink)}
  .headline__lead{font-family:"Cormorant Garamond",Georgia,serif;font-size:19px;letter-spacing:2px;text-transform:uppercase}
  .headline__script{font-family:"Great Vibes",cursive;font-size:64px;line-height:1;margin-top:-4px}
  .headline__script small{font-size:28px;vertical-align:top;margin-right:4px}
  .name-box{position:absolute;left:20px;bottom:22px;background:var(--navy);border-radius:18px;padding:10px 22px;color:var(--white)}
  .name-box__name{font-size:18px}
  .name-box__phone{font-size:11px;display:flex;align-items:center;gap:5px}
  .name-box__phone svg{width:11px;height:11px}
  .badges{position:absolute;right:18px;bottom:18px;display:flex;gap:10px;align-items:flex-end}
  .badge-tile{width:62px;height:56px;border-radius:12px;background:var(--white);border:4px solid var(--brown);display:flex;align-items:center;justify-content:center;font-size:9px;font-weight:600;color:var(--navy)}
  .badge-partner{width:72px;height:56px;background:var(--maroon)}
</style>
</head>
<body>

<section class="card card--back">
  <div class="brand-tile">
    <span class="brand-tile__mark"></span>
    <span class="brand-tile__name">Stable Arc</span>
  </div>

  <div class="contact contact--top">
    <div class="contact__row">
      <svg class="icon" viewBox="0 0 24 24"><circle cx="12" cy="12" r="12" fill="var(--navy)"/><path d="M8.5 6.5l2 2-1.2 1.6c.8 1.7 2 2.9 3.6 3.6l1.6-1.2 2 2-1.5 1.8C11 15.8 8.2 13 7 9z" fill="#fff"/></svg>
      <span>0438 512 607</span>
    </div>
    <div class="contact__row">
      <svg class="icon" viewBox="0 0 24 24"><circle cx="12" cy="12" r="12" fill="var(--navy)"/><rect x="6" y="8" width="12" height="8" fill="none" stroke="#fff" stroke-width="1.3"/><path d="M6 8l6 5 6-5" fill="none" stroke="#fff" stroke-width="1.3"/></svg>
      <span>lbrand@fauna812.com.au</span>
    </div>
  </div>

  <div class="contact contact--bottom">
    <div class="contact__row">
      <svg class="icon" viewBox="0 0 24 24"><circle cx="12" cy="12" r="12" fill="var(--navy)"/></svg>
      <span>FB/lewis.brand.207</span>
    </div>
    <div class="contact__row">
      <svg class="icon" viewBox="0 0 24 24"><circle cx="12" cy="12" r="12" fill="var(--navy)"/><circle cx="12" cy="12" r="6.5" fill="none" stroke="#fff" stroke-width="1.2"/><ellipse cx="12" cy="12" rx="3" ry="6.5" fill="none" stroke="#fff" stroke-width="1.2"/><path d="M5.5 12h13" stroke="#fff" stroke-width="1.2"/></svg>
      <span>www.StableArc.com.au</span>
    </div>
  </div>

  <div class="details">
    <h1 class="details__name">Lewis Brand</h1>
    <ul class="details__list">
      <li><svg viewBox="0 0 12 12"><path d="M1.5 6.5l3 3 6-7" fill="none" stroke="#fff" stroke-width="2"/></svg>Equine Performance</li>
      <li><svg viewBox="0 0 12 12"><path d="M1.5 6.5l3 3 6-7" fill="none" stroke="#fff" stroke-width="2"/></svg>Rowland4Ponies and Acupuncture</li>
      <li><svg viewBox="0 0 12 12"><path d="M1.5 6.5l3 3 6-7" fill="none" stroke="#fff" stroke-width="2"/></svg>Horsemanship Lessons and Clinics</li>
      <li><svg viewBox="0 0 12 12"><path d="M1.5 6.5l3 3 6-7" fill="none" stroke="#fff" stroke-width="2"/></svg>Horse Training</li>
    </ul>
  </div>
</section>

<section class="card card--front">
  <div class="photo" role="img" aria-label="Photo of a trainer and a handler working a bay horse in a sandy arena"></div>
  <div class="headline">
    <p class="headline__lead">How you ever gonna know</p>
    <p class="headline__script"><small>Your</small>Potential</p>
  </div>
  <div class="name-box">
    <p class="name-box__name">Lewis Brand</p>
    <p class="name-box__phone"><svg viewBox="0 0 12 12"><path d="M2.5 1l2 2-1 1.4c.6 1.5 1.6 2.5 3.1 3.1l1.4-1 2 2-1.4 1.6C4.8 9.6 2.4 7.2 1 2.4z" fill="#fff"/></svg>0438 512 607</p>
  </div>
  <div class="badges">
    <div class="badge-tile">Stable Arc</div>
    <div class="badge-partner" role="img" aria-label="Neil Patton Practitioner Group badge"></div>
  </div>
</section>

</body>
</html>
```